Lanternfold Advisory Business Cards

We need a new layout for our business cards. We have a logo already. But we might be interested in only using the Lanternfold portion of the logo. It has been uploaded.

We would like cards that are not overly busy. Clean. Modern. Perhaps a gray color for one side.

On the back, we would like to have the lanternfold part of the logo and "Step forward, we stand ready!"

Our business provides medics and safety training for corporate clients. Our website is www.lanternfoldadvisoryllc.example.

Industry/Entity Type

Business

Contact Information for Business Card

We want include name, email address, cell phone, main line number, and website URL on the front. Use the following as an example: Dana Kovrin, dana@lanternfoldadvisoryllc.example, 804.321.7788 (cell), 804.432.919, and www.lanternfoldadvisoryllc.example.

Font styles to use
Serif
Sans Serif

Requirements
Must have
• All required information. Back side logo with "Take the leap, we will catch you!"
Nice to have
• If possible, we would like to consider creating a card in a non-standard shape. Perhaps, the shape of a lanternfold. Just interested in understanding the option.

```html
<!DOCTYPE html>
<html lang="en">
<head>
<meta charset="utf-8">
<title>Lanternfold Advisory Business Cards</title>
<link rel="stylesheet" href="https://fonts.googleapis.com/css2?family=Libre+Baskerville&family=Montserrat:wght@400;600&display=swap">
<style>
  :root {
    --brand-blue: #0b4f95;
    --card-white: #ffffff;
    --ink: #1c1c1c;
    --muted: #555a60;
    --stage: #e6e7e9;
  }
  * { box-sizing: border-box; margin: 0; padding: 0; }
  html, body { width: 1200px; height: 900px; overflow: hidden; }
  body { background: var(--stage); position: relative; font-family: "Montserrat", sans-serif; }

  .card {
    position: absolute;
    width: 600px;
    height: 340px;
    border-radius: 18px;
    overflow: hidden;
    box-shadow: 0 10px 28px rgba(0,0,0,0.18);
  }
  .card-shape { position: absolute; inset: 0; }

  /* Back side */
  .card-back { left: 90px; top: 70px; background: var(--brand-blue); }
  .back-mark {
    position: absolute; left: 0; right: 0; top: 96px;
    display: flex; align-items: center; justify-content: center; gap: 14px;
  }
  .back-mark .dot { width: 16px; height: 16px; border-radius: 50%; background: var(--card-white); }
  .back-mark .wordmark {
    font-family: "Montserrat", sans-serif; font-weight: 600; font-size: 32px;
    color: var(--card-white);
  }
  .back-tagline {
    position: absolute; left: 0; right: 0; top: 206px; text-align: center;
    font-weight: 600; font-size: 15px; letter-spacing: 1.2px;
    color: var(--card-white); text-transform: uppercase;
  }

  /* Front side */
  .card-front { left: 510px; top: 480px; background: var(--card-white); }
  .holder-name {
    position: absolute; right: 44px; top: 46px;
    font-family: "Libre Baskerville", serif; font-weight: 400; font-size: 22px;
    color: var(--brand-blue); text-transform: uppercase; letter-spacing: 0.5px;
  }
  .logo-block { position: absolute; left: 44px; top: 126px; }
  .logo-row { display: flex; align-items: center; gap: 10px; }
  .logo-row .dot { width: 14px; height: 14px; border-radius: 50%; background: var(--brand-blue); }
  .logo-row .wordmark {
    font-family: "Montserrat", sans-serif; font-weight: 600; font-size: 22px; color: var(--ink);
  }
  .contact-list {
    position: absolute; left: 44px; top: 226px; list-style: none;
    font-size: 13px; color: var(--ink); line-height: 21px;
  }
  .contact-list li { display: flex; align-items: center; gap: 10px; }
  .contact-list svg { width: 12px; height: 12px; fill: var(--brand-blue); flex: none; }
  .contact-list .domain { color: var(--brand-blue); font-weight: 600; }
</style>
</head>
<body>

<section class="card card-back" aria-label="Card back">
  <svg class="card-shape" viewBox="0 0 600 340" aria-hidden="true">
    <polygon points="0,266 322,266 352,250 392,340 0,340" fill="#ffffff"/>
  </svg>
  <div class="back-mark">
    <span class="dot"></span>
    <span class="wordmark">Lanternfold</span>
  </div>
  <p class="back-tagline">Step forward, we stand ready</p>
</section>

<section class="card card-front" aria-label="Card front">
  <svg class="card-shape" viewBox="0 0 600 340" aria-hidden="true">
    <rect x="570" y="44" width="30" height="26" fill="#0b4f95"/>
    <line x1="190" y1="84" x2="570" y2="84" stroke="#1c1c1c" stroke-width="1.5"/>
    <polygon points="420,200 600,200 600,262 404,262" fill="#0b4f95"/>
    <line x1="44" y1="216" x2="330" y2="216" stroke="#1c1c1c" stroke-width="1.5"/>
  </svg>

  <h1 class="holder-name">Dana Kovrin</h1>

  <div class="logo-block">
    <div class="logo-row">
      <span class="dot"></span>
      <span class="wordmark">Lanternfold Advisory</span>
    </div>
  </div>

  <ul class="contact-list">
    <li>
      <svg viewBox="0 0 12 12"><path d="M3 0h6a1 1 0 0 1 1 1v10a1 1 0 0 1-1 1H3a1 1 0 0 1-1-1V1a1 1 0 0 1 1-1zm0 2v7h6V2z"/></svg>
      804.321.7788
    </li>
    <li>
      <svg viewBox="0 0 12 12"><path d="M2.4 0.5l2 2.2-1 1.4c.7 1.6 2 2.9 3.5 3.6l1.4-1 2.2 2-1.1 2.3C5 10.8 1.2 7 0.5 1.6z"/></svg>
      804.432.919(main)
    </li>
    <li>
      <svg viewBox="0 0 12 12"><path d="M0 2h12v8H0zm1 1v.4l5 3.2 5-3.2V3zm0 1.6V9h10V4.6L6 7.8z"/></svg>
      dana@lanternfoldadvisoryllc.example
    </li>
    <li>
      <svg viewBox="0 0 12 12"><circle cx="6" cy="6" r="5.3" fill="none" stroke="#0b4f95" stroke-width="1.2"/><path d="M0.7 5.4h10.6v1.2H0.7zM5.4 0.7h1.2v10.6H5.4z"/></svg>
      <span>www.<span class="domain">lanternfoldadvisoryllc.example</span></span>
    </li>
  </ul>
</section>

</body>
</html>
```